Business cards for Remote DBA team

Business cards for team offering database administration, consultation, machine learning and AI services. As of now team is using both
www.korvilnet.cz and www.brestmoorlab.cz URLs

Target Market(s)

IT managers

Industry/Entity Type

It Professional

Contact Information for Business Card

Should include logo
name, email, phone, twitter tag

Font styles to use
Sans Serif

Colors

Designer to choose colors to be used in the design.

```html
<!DOCTYPE html>
<html lang="en">
<head>
<meta charset="utf-8">
<title>Korvil Data Lab – Business Card</title>
<link href="https://fonts.googleapis.com/css2?family=Montserrat:wght@700&family=Roboto:wght@400;500&display=swap" rel="stylesheet">
<style>
  :root {
    --page-bg: #e7e5e2;
    --card-top: #e9e6e1;
    --card-bottom: #d9d4cd;
    --brand-blue: #1f4f82;
    --band-blue-1: #2c6aa3;
    --band-blue-2: #1c4f80;
    --band-dark: #4b4642;
    --name-text: #e3e9ef;
    --contact-text: #d9d5d0;
    --icon: #e6e2dd;
  }
  html, body {
    margin: 0;
    padding: 0;
    width: 1200px;
    height: 969px;
    overflow: hidden;
    background: var(--page-bg);
  }
  .card {
    position: absolute;
    left: 100px;
    top: 200px;
    width: 1000px;
    height: 570px;
    background: linear-gradient(180deg, var(--card-top), var(--card-bottom));
    box-shadow: 0 6px 24px rgba(0,0,0,0.12);
    overflow: hidden;
  }
  .brand {
    position: absolute;
    left: 262px;
    top: 96px;
    display: flex;
    align-items: center;
    gap: 28px;
  }
  .brand-dot {
    width: 110px;
    height: 110px;
    border-radius: 50%;
    background: var(--brand-blue);
  }
  .brand-name {
    margin: 0;
    font-family: 'Montserrat', sans-serif;
    font-weight: 700;
    font-size: 60px;
    line-height: 58px;
    letter-spacing: 0.5px;
    color: var(--brand-blue);
  }
  .contact-band {
    position: absolute;
    left: 0;
    top: 344px;
    width: 1000px;
    height: 181px;
  }
  .holder-name {
    position: absolute;
    left: 46px;
    top: 410px;
    margin: 0;
    font-family: 'Roboto', sans-serif;
    font-weight: 500;
    font-size: 32px;
    letter-spacing: 0.5px;
    color: var(--name-text);
  }
  .contact-list {
    position: absolute;
    right: 38px;
    top: 364px;
    margin: 0;
    padding: 0;
    list-style: none;
    font-family: 'Roboto', sans-serif;
    font-size: 21px;
    color: var(--contact-text);
  }
  .contact-item {
    display: flex;
    justify-content: flex-end;
    align-items: center;
    gap: 18px;
    height: 31px;
  }
  .contact-icon {
    width: 20px;
    height: 20px;
    flex: none;
  }
</style>
</head>
<body>
  <main class="card">
    <div class="brand">
      <div class="brand-dot"></div>
      <h1 class="brand-name">KORVIL<br>DATA<br>LAB</h1>
    </div>

    <svg class="contact-band" viewBox="0 0 1000 181" aria-hidden="true">
      <defs>
        <linearGradient id="blueBand" x1="0" y1="0" x2="0" y2="1">
          <stop offset="0" stop-color="var(--band-blue-1)"/>
          <stop offset="1" stop-color="var(--band-blue-2)"/>
        </linearGradient>
      </defs>
      <rect x="0" y="0" width="1000" height="181" fill="var(--band-dark)"/>
      <polygon points="0,0 511,0 466,181 0,181" fill="url(#blueBand)"/>
      <line x1="511" y1="0" x2="466" y2="181" stroke="#c9b9a6" stroke-width="1.5" opacity="0.7"/>
    </svg>

    <p class="holder-name">TOMAS VERHAL</p>

    <ul class="contact-list">
      <li class="contact-item">604 218 7395
        <svg class="contact-icon" viewBox="0 0 20 20" aria-hidden="true"><path d="M5 2 L8 6 L6.5 8 Q8 12 12 13.5 L14 12 L18 15 L16 18 Q9 18 5 13 Q2 9 2 4 Z" fill="var(--icon)"/></svg>
      </li>
      <li class="contact-item">hello@korvildata.com
        <svg class="contact-icon" viewBox="0 0 20 20" aria-hidden="true"><rect x="2" y="5" width="16" height="11" fill="var(--icon)"/><path d="M2 5 L10 11 L18 5" stroke="var(--band-dark)" stroke-width="1.4" fill="none"/></svg>
      </li>
      <li class="contact-item">www.brestmoorlab.cz
        <svg class="contact-icon" viewBox="0 0 20 20" aria-hidden="true"><circle cx="10" cy="10" r="8" fill="none" stroke="var(--icon)" stroke-width="1.8"/><ellipse cx="10" cy="10" rx="3.5" ry="8" fill="none" stroke="var(--icon)" stroke-width="1.4"/><line x1="2" y1="10" x2="18" y2="10" stroke="var(--icon)" stroke-width="1.4"/></svg>
      </li>
      <li class="contact-item">www.korvilnet.cz
        <svg class="contact-icon" viewBox="0 0 20 20" aria-hidden="true"><circle cx="10" cy="10" r="7.5" fill="var(--icon)"/></svg>
      </li>
    </ul>
  </main>
</body>
</html>
```